Business Card for premium dental clinic

We are a premium dental clinic based in Brasov, Romania with more than 15 year on the market, providing quality dental treatment made by a team of more specialized dentists, working with modern equipment as a solution to beautiful and healthy teeth.

Our current logo for the clinic use 2 square with colors black and gold - dr Corbescu - studio, using family fonts Bodoni, Myriad Pro and Segoe Print.
Depending on the printing we used some gold CMYK background or gold foil picture background or a gold gradient.
We want a business card:
- eye catching business card
- distinguished business card
- premium design
- to keep the color scheme of black and gold
- to attract the customers to spent time reading the information
- modern concept

```html
<!DOCTYPE html>
<html lang="en">
<head>
<meta charset="utf-8">
<title>Dental Clinic Business Card</title>
<link rel="stylesheet" href="https://fonts.googleapis.com/css2?family=Fira+Sans+Condensed:wght@400;500&family=Questrial&display=swap">
<style>
  :root {
    --backdrop: #2b2e33;
    --card-black: #0b0b0b;
    --gold-light: #f3d36a;
    --gold-mid: #d9a521;
    --gold-deep: #a8760e;
    --line-white: #f5f5f5;
    --text-white: #ffffff;
    --icon-gold: #e0ad2c;
  }
  * { margin: 0; padding: 0; box-sizing: border-box; }
  html, body { width: 1200px; height: 1000px; overflow: hidden; }
  body { background: var(--backdrop); position: relative; font-family: "Questrial", sans-serif; }

  .card {
    position: absolute;
    width: 720px;
    height: 410px;
    left: 240px;
    background: var(--card-black);
    overflow: hidden;
    box-shadow: 0 12px 30px rgba(0,0,0,0.45);
  }
  .card--front { top: 60px; }
  .card--back { top: 530px; }

  .gold-fill {
    position: absolute;
    background: linear-gradient(135deg, var(--gold-light) 0%, var(--gold-mid) 45%, var(--gold-deep) 70%, var(--gold-mid) 100%);
  }

  /* Front */
  .front-gold { left: 0; top: 0; width: 360px; height: 410px; }
  .front-frame {
    position: absolute; left: 150px; top: 95px; width: 480px; height: 240px;
    border: 2px solid var(--line-white);
  }
  .brand-name {
    position: absolute;
    font-family: "Fira Sans Condensed", sans-serif;
    font-weight: 400;
    color: var(--text-white);
    white-space: nowrap;
    line-height: 1;
  }
  .front-name { left: 378px; top: 182px; font-size: 28px; }
  .tagline {
    position: absolute;
    font-family: "Fira Sans Condensed", sans-serif;
    font-weight: 500;
    color: var(--text-white);
    white-space: nowrap;
    line-height: 1;
  }
  .front-tagline { right: 110px; top: 290px; font-size: 22px; }

  /* Back */
  .back-border { left: 0; top: 0; width: 720px; height: 410px; }
  .back-panel {
    position: absolute; left: 26px; top: 26px; width: 668px; height: 358px;
    background: var(--card-black);
  }
  .back-frame {
    position: absolute; left: 36px; top: 36px; width: 648px; height: 338px;
    border: 1.5px solid var(--line-white);
  }
  .logo-block {
    position: absolute; left: 82px; top: 140px; width: 320px; height: 140px;
  }
  .logo-gold { left: 0; top: 0; width: 120px; height: 140px; }
  .logo-black { position: absolute; left: 120px; top: 0; width: 200px; height: 140px; background: var(--card-black); }
  .logo-frame { position: absolute; inset: 0; border: 1.5px solid var(--line-white); }
  .back-name { left: 132px; top: 42px; font-size: 21px; }
  .back-tagline { right: 12px; bottom: 14px; font-size: 15px; }

  .contact-list {
    position: absolute; left: 440px; top: 140px;
    list-style: none;
    color: var(--text-white);
    font-size: 16px;
    line-height: 1.35;
    letter-spacing: 0.3px;
  }
  .contact-item { display: flex; align-items: center; gap: 8px; }
  .contact-item svg { width: 15px; height: 15px; flex: none; }
  .contact-address { margin-top: 6px; }
</style>
</head>
<body>

<section class="card card--front">
  <div class="gold-fill front-gold" role="img" aria-label="Gold foil texture panel"></div>
  <div class="front-frame"></div>
  <div class="brand-name front-name">dr Corbescu studio</div>
  <div class="tagline front-tagline">dental clinic</div>
</section>

<section class="card card--back">
  <div class="gold-fill back-border" role="img" aria-label="Gold foil texture border"></div>
  <div class="back-panel"></div>
  <div class="back-frame"></div>

  <div class="logo-block">
    <div class="gold-fill logo-gold" role="img" aria-label="Gold foil texture square"></div>
    <div class="logo-black"></div>
    <div class="logo-frame"></div>
    <div class="brand-name back-name">dr Corbescu studio</div>
    <div class="tagline back-tagline">dental clinic</div>
  </div>

  <ul class="contact-list">
    <li class="contact-item">
      <svg viewBox="0 0 16 16" aria-hidden="true"><path fill="var(--icon-gold)" d="M3.6 1.2l2.2 2.6-1.2 1.7c.9 2 2.3 3.4 4.2 4.3l1.7-1.2 2.6 2.2-1.1 2.6C7 13.5 2.4 8.9 2.4 3.2z"/></svg>
      <span>555-302-1187</span>
    </li>
    <li class="contact-item">
      <svg viewBox="0 0 16 16" aria-hidden="true"><rect x="1" y="3" width="14" height="10" fill="var(--icon-gold)"/><path d="M1.5 3.5L8 9l6.5-5.5" fill="none" stroke="var(--card-black)" stroke-width="1.2"/></svg>
      <span>555-302-1187</span>
    </li>
    <li class="contact-item">
      <svg viewBox="0 0 16 16" aria-hidden="true"><rect x="4" y="1.5" width="8" height="4" fill="var(--icon-gold)"/><rect x="1" y="6" width="14" height="6" fill="var(--icon-gold)"/><rect x="4" y="10" width="8" height="4.5" fill="var(--icon-gold)" stroke="var(--card-black)" stroke-width="1"/></svg>
      <span>elena@smilemail.com</span>
    </li>
    <li class="contact-address">18 Lindenwood Street NE<br>Suite 200, Cedar Falls<br>MI 49210</li>
  </ul>
</section>

</body>
</html>
```